Luxury Real Estate Website, Midwest, United States

We need web design services for a luxury website. We need IDX Integration with our MLS. We want this to be a very simple website with amazing graphics. We want it to link up with our MailChimp account in order to generate leads through a "More Information" Pop up on the main page. We want the main page to be covered with one large graphic that is a rolling slideshow of active listings of $400,000 and up from the IDX Integration. We need this website to give a very exclusive and sleek look. Lots of black is good... I will upload our logos in Black and Silver. We will also need an "About" page that we are going to call "MyQV Info". We want our graphics to be extremely impressive. Keep in mind, we are a company in the Midwest of the United States, and our real estate has a different look than homes in California or Florida. We need graphics that are realistic for the Midwest, yet still high-end.
Target Market(s)
Luxury Homeowners in the Midwest United States. The graphics needs to be pristine.
Industry/Entity Type
Real Estate
Coding
Coded - Design and coding required
Number of Pages Required
3 page
Requirements
Must have
- Large graphics with IDX Integration. The photos of real estate need to represent real estate that is common in the Midwest, United States. We also need MailChimp integration. We need a pop up that is titled "My Free Market Analysis" that makes them fill out a contact form asking for Full Name, Email Address, Phone Number and Address. This needs to be a pop up on the front page and will integrate with our MailChimp account. We also need a page called "About My QV Home". And another page where clients can download informational PDFs. The main component needs to be a front page search engine connected with the IDX to access active listings from our MLS. I attached our logos and a sample front page of a website. I would love for ours to look similar.
Nice to have
- Lake House photos on midwest lakes are a plus.
Should not have
- Should not have clutter. This website needs to be clean, luxurious and exclusive.

```html
<!DOCTYPE html>
<html lang="en">
<head>
<meta charset="utf-8">
<title>Hearthside Realty Group</title>
<link href="https://fonts.googleapis.com/css2?family=Roboto+Condensed:wght@400;700&family=Roboto:ital,wght@0,400;0,500;0,700;1,400&display=swap" rel="stylesheet">
<style>
:root{
  --ink:#1d1d1d;
  --text:#555;
  --muted:#8a8a8a;
  --line:#dcdcdc;
  --paper:#ffffff;
  --mist:#f2f2f2;
  --night:#121212;
  --black:#050505;
  --accent:#3f7fc1;
  --tag:#5b93c9;
}
*{box-sizing:border-box;margin:0;padding:0}
html,body{width:1200px;height:3208px;overflow:hidden}
body{font-family:"Roboto",Arial,sans-serif;color:var(--text);background:var(--paper);font-size:13px;line-height:1.6}
h1,h2,h3,.nav a,.btn{font-family:"Roboto Condensed","Arial Narrow",sans-serif}
a{color:inherit;text-decoration:none}

/* header */
.site-header{height:100px;display:flex;align-items:center;justify-content:space-between;padding:0 130px 0 128px;background:var(--paper)}
.brand{display:flex;align-items:center;gap:10px;font-family:"Roboto Condensed",sans-serif;font-weight:700;color:var(--ink);font-size:22px;letter-spacing:1px;line-height:1}
.brand-square{width:14px;height:14px;background:var(--ink)}
.nav{display:flex;gap:34px}
.nav a{font-size:13px;font-weight:700;color:var(--ink);letter-spacing:.5px}

/* hero */
.hero{position:relative;height:480px;overflow:hidden}
.hero-photo{position:absolute;inset:0;background:linear-gradient(180deg,#33485e 0%,#5e7488 32%,#3c5237 58%,#2a3a2a 66%,#4c6171 78%,#263444 100%)}
.hero-shade{position:absolute;inset:0;background:rgba(0,0,0,.22)}
.hero-content{position:relative;text-align:center;color:#fff;padding-top:168px}
.hero h1{font-size:46px;font-weight:700;letter-spacing:1px;line-height:1.1}
.hero p{font-size:15px;margin:14px auto 0;width:340px;line-height:1.45}
.search{width:410px;height:40px;margin:26px auto 0;background:#fff;display:flex;align-items:center;justify-content:space-between;padding-left:14px;font-size:12px;color:#777}
.search-btn{width:40px;height:40px;background:var(--accent);display:flex;align-items:center;justify-content:center}
.hero-arrow{position:absolute;top:240px;width:30px;height:30px;border-radius:50%;background:rgba(0,0,0,.55);display:flex;align-items:center;justify-content:center}
.hero-arrow.prev{left:98px}.hero-arrow.next{right:98px}
.hero-curve{position:absolute;left:0;bottom:0;width:1200px;height:110px}

/* features */
.features{height:560px;display:flex;justify-content:center;align-items:flex-start;padding-top:80px}
.feature{width:300px;text-align:center;padding:110px 26px 0}
.feature.raised{width:336px;height:440px;margin:0 18px;background:#fff;box-shadow:0 6px 28px rgba(0,0,0,.16);padding-top:110px}
.feature-icon{width:62px;height:62px;border-radius:50%;background:#ededed;margin:0 auto 22px;display:flex;align-items:center;justify-content:center}
.feature h3{font-family:"Roboto",sans-serif;font-size:17px;font-weight:500;color:var(--ink);margin-bottom:10px}
.feature p{font-size:12px;color:var(--muted);line-height:1.65;width:230px;margin:0 auto}
.btn-small{display:inline-block;margin-top:18px;border:1px solid #999;border-radius:12px;padding:2px 14px;font-size:11px;color:var(--ink)}

/* welcome */
.welcome{position:relative;height:400px;color:#fff;text-align:center;overflow:hidden}
.welcome-photo{position:absolute;inset:0;background:linear-gradient(100deg,#0c0c0c 0%,#23211d 35%,#151513 60%,#2a2822 85%,#0d0d0d 100%)}
.welcome-content{position:relative;padding-top:96px}
.welcome h2{font-size:36px;font-weight:700;letter-spacing:.5px}
.welcome p{width:780px;margin:16px auto 0;font-size:12.5px;line-height:1.75;color:#d6d6d6}
.btn-outline{display:inline-block;margin-top:26px;border:1px solid #fff;padding:7px 20px;font-size:12px;font-weight:700;letter-spacing:1px}

/* listings */
.listings{height:890px;background:var(--mist);padding-top:78px}
.section-title{font-size:30px;font-weight:700;color:var(--ink);text-align:center;letter-spacing:.5px}
.listing-grid{display:grid;grid-template-columns:repeat(3,296px);column-gap:24px;row-gap:42px;width:936px;margin:42px auto 0}
.listing{background:#fff;height:300px;box-shadow:0 1px 4px rgba(0,0,0,.08)}
.listing-photo{position:relative;height:150px;border:3px solid #fff}
.listing-tag{position:absolute;top:10px;right:0;background:var(--tag);color:#fff;font-size:9px;font-weight:700;padding:2px 8px;letter-spacing:.5px}
.listing-body{padding:10px 16px 0;font-size:11px;color:var(--muted);line-height:1.6;height:92px}
.listing-foot{display:flex;justify-content:space-between;align-items:center;border-top:1px solid #eee;margin:0 16px;padding-top:12px;font-size:11px;color:#666}
.listing-foot span{display:flex;align-items:center;gap:5px}
.p1{background:linear-gradient(180deg,#6f94bd 0%,#a7bfd6 45%,#6d6a63 70%,#4d6b3c 100%)}
.p2{background:linear-gradient(180deg,#8fb3d6 0%,#c9d6df 40%,#a89c84 65%,#5e8a3e 100%)}
.p3{background:linear-gradient(180deg,#7fa6cf 0%,#d8dde0 45%,#eaeae6 65%,#6f8f5a 100%)}
.p4{background:linear-gradient(180deg,#84a9cd 0%,#b9c9d6 40%,#8c7d6c 68%,#4f7c37 100%)}
.p5{background:linear-gradient(180deg,#5d8ec4 0%,#9dbb6a 40%,#b59262 65%,#5b8c35 100%)}
.p6{background:linear-gradient(180deg,#9fb8d0 0%,#c4b39c 45%,#8a6c52 70%,#637a4a 100%)}

/* news */
.news{height:400px;padding:66px 132px 0}
.news-head{display:flex;justify-content:space-between;align-items:center}
.news-head h2{font-size:24px;font-weight:700;color:var(--ink);letter-spacing:.5px}
.news-arrows{display:flex;gap:12px}
.news-list{display:flex;gap:58px;margin-top:36px}
.news-item{display:flex;gap:22px;width:440px}
.news-photo{width:170px;height:140px;flex:none}
.n1{background:linear-gradient(180deg,#8eb3d9 0%,#c3cfd8 45%,#90806a 70%,#6e9a4c 100%)}
.n2{background:linear-gradient(160deg,#6e9bc8 0%,#a0b985 50%,#c9a27c 75%,#5b7f3f 100%)}
.news-item h3{font-family:"Roboto",sans-serif;font-style:italic;font-weight:400;font-size:14px;color:#777}
.news-date{font-size:10px;font-weight:700;color:var(--ink);margin:6px 0 6px;letter-spacing:.5px}
.news-item p{font-size:11px;color:var(--muted);line-height:1.6}
.news-more{display:inline-block;margin-top:8px;font-size:11px;font-weight:500;color:var(--ink)}

/* footer */
.site-footer{height:330px;background:var(--night);color:#c8c8c8;display:flex;padding:46px 132px 0;gap:0}
.footer-brand{width:230px;padding-top:28px}
.footer-brand .brand{color:#fff;font-size:18px}
.footer-brand .brand-square{background:#fff;width:12px;height:12px}
.social{display:flex;gap:8px;margin-top:20px}
.social span{width:20px;height:20px;border-radius:50%;background:#e6e6e6}
.footer-col{font-size:11px}
.footer-col h3{color:#fff;font-size:15px;font-weight:700;letter-spacing:.5px;margin-bottom:18px}
.contact{width:280px}
.contact li{list-style:none;display:flex;gap:10px;margin-bottom:10px;line-height:1.5}
.signup{width:300px}
.signup p{width:220px;line-height:1.55}
.signup-input{width:150px;height:26px;background:#fff;color:#999;font-size:10px;padding:5px 8px;margin-top:14px}
.signup-btn{display:inline-block;margin-top:10px;background:#3a3a3a;color:#fff;font-size:10px;font-weight:700;padding:5px 12px;letter-spacing:.5px}
.quick ul{list-style:none}
.quick li{margin-bottom:8px}
.copyright{height:48px;background:var(--black);color:#888;font-size:10px;text-align:center;line-height:48px}
</style>
</head>
<body>

<header class="site-header">
  <a class="brand" href="#"><span class="brand-square"></span>HEARTHSIDE REALTY GROUP</a>
  <nav class="nav">
    <a href="#">HOME</a>
    <a href="#">MYQV INFO</a>
    <a href="#">ABOUT MY QV HOME</a>
    <a href="#">DOWNLOADS</a>
    <a href="#">CONTACT US</a>
  </nav>
</header>

<section class="hero">
  <div class="hero-photo" role="img" aria-label="Lakeside Midwest home at dusk among trees, reflected in still water"></div>
  <div class="hero-shade"></div>
  <div class="hero-content">
    <h1>HEARTHSIDE REALTY GROUP</h1>
    <p>Lorem ipsum dolor sit amet conse ctetur adipiscing elit, do eiusmod</p>
    <div class="search">Search homes by city &amp; state, zip
      <span class="search-btn"><svg width="16" height="16" viewBox="0 0 16 16"><circle cx="6.5" cy="6.5" r="4.5" fill="none" stroke="#fff" stroke-width="2"/><line x1="10" y1="10" x2="14" y2="14" stroke="#fff" stroke-width="2"/></svg></span>
    </div>
  </div>
  <span class="hero-arrow prev"><svg width="10" height="12" viewBox="0 0 10 12"><path d="M7 1 2 6l5 5" fill="none" stroke="#fff" stroke-width="2"/></svg></span>
  <span class="hero-arrow next"><svg width="10" height="12" viewBox="0 0 10 12"><path d="M3 1l5 5-5 5" fill="none" stroke="#fff" stroke-width="2"/></svg></span>
  <svg class="hero-curve" viewBox="0 0 1200 110" preserveAspectRatio="none">
    <path d="M0 30 Q600 150 1200 30 L1200 110 L0 110Z" fill="#ffffff"/>
    <path d="M0 30 Q600 150 1200 30" fill="none" stroke="#b9b9b9" stroke-width="6"/>
    <path d="M0 42 Q600 150 1200 42" fill="none" stroke="#e4e4e4" stroke-width="3"/>
  </svg>
</section>

<section class="features">
  <div class="feature">
    <div class="feature-icon"><svg width="30" height="30" viewBox="0 0 30 30"><path d="M4 15 15 5l11 10M8 12v12h14V12" fill="none" stroke="#333" stroke-width="2"/><rect x="13" y="17" width="4" height="7" fill="#333"/></svg></div>
    <h3>Quis autem vel eum</h3>
    <p>Browse active listings across our region, with fresh photos, clear pricing and honest advice from a local team.</p>
    <a class="btn-small" href="#">Read More</a>
  </div>
  <div class="feature raised">
    <div class="feature-icon"><svg width="30" height="30" viewBox="0 0 30 30"><path d="M5 5h10l10 10-10 10L5 15Z" fill="none" stroke="#333" stroke-width="2"/><circle cx="10" cy="10" r="2" fill="#333"/></svg></div>
    <h3>Quis autem vel eum</h3>
    <p>Learn what your home is worth today with a free market review prepared by agents who know your neighborhood.</p>
    <a class="btn-small" href="#">Read More</a>
  </div>
  <div class="feature">
    <div class="feature-icon"><svg width="30" height="30" viewBox="0 0 30 30"><rect x="4" y="6" width="22" height="15" fill="none" stroke="#333" stroke-width="2"/><path d="M11 25h8M15 21v4" stroke="#333" stroke-width="2"/></svg></div>
    <h3>Quis autem vel eum</h3>
    <p>Download our buyer and seller guides, checklists and market reports to plan every step of your next move.</p>
    <a class="btn-small" href="#">Read More</a>
  </div>
</section>

<section class="welcome">
  <div class="welcome-photo" role="img" aria-label="Dark evening view of a wooded lakeside estate"></div>
  <div class="welcome-content">
    <h2>WELCOME TO HEARTHSIDE REALTY GROUP</h2>
    <p>We help families buy and sell fine homes across the Midwest, from lakeside retreats to quiet estates. Our agents know every street, school and shoreline, and we guide each client with care from the first showing to the final signature. Call us today to start your search.</p>
    <a class="btn-outline" href="#">READ MORE</a>
  </div>
</section>

<section class="listings">
  <h2 class="section-title">PROPERTIES LISTINGS</h2>
  <div class="listing-grid">
    <article class="listing">
      <div class="listing-photo p1" role="img" aria-label="Two-storey modern home with lit windows"><span class="listing-tag">NEW LISTING</span></div>
      <div class="listing-body">Four bedrooms, open kitchen and a wide deck facing the water, set on a quiet wooded lot.</div>
      <div class="listing-foot"><span><svg width="9" height="12" viewBox="0 0 9 12"><path d="M4.5 0C2 0 0 2 0 4.5 0 8 4.5 12 4.5 12S9 8 9 4.5C9 2 7 0 4.5 0Z" fill="#555"/><circle cx="4.5" cy="4.5" r="1.6" fill="#fff"/></svg>Los Angeles, California</span><b>$470,000</b></div>
    </article>
    <article class="listing">
      <div class="listing-photo p2" role="img" aria-label="Suburban family home with green lawn"><span class="listing-tag">NEW LISTING</span></div>
      <div class="listing-body">Four bedrooms, open kitchen and a wide deck facing the water, set on a quiet wooded lot.</div>
      <div class="listing-foot"><span><svg width="9" height="12" viewBox="0 0 9 12"><path d="M4.5 0C2 0 0 2 0 4.5 0 8 4.5 12 4.5 12S9 8 9 4.5C9 2 7 0 4.5 0Z" fill="#555"/><circle cx="4.5" cy="4.5" r="1.6" fill="#fff"/></svg>Los Angeles, California</span><b>$520,000</b></div>
    </article>
    <article class="listing">
      <div class="listing-photo p3" role="img" aria-label="White colonial house with porch"><span class="listing-tag">NEW LISTING</span></div>
      <div class="listing-body">Four bedrooms, open kitchen and a wide deck facing the water, set on a quiet wooded lot.</div>
      <div class="listing-foot"><span><svg width="9" height="12" viewBox="0 0 9 12"><path d="M4.5 0C2 0 0 2 0 4.5 0 8 4.5 12 4.5 12S9 8 9 4.5C9 2 7 0 4.5 0Z" fill="#555"/><circle cx="4.5" cy="4.5" r="1.6" fill="#fff"/></svg>Los Angeles, California</span><b>$610,000</b></div>
    </article>
    <article class="listing">
      <div class="listing-photo p4" role="img" aria-label="Brick family home with front garden"><span class="listing-tag">NEW LISTING</span></div>
      <div class="listing-body">Four bedrooms, open kitchen and a wide deck facing the water, set on a quiet wooded lot.</div>
      <div class="listing-foot"><span><svg width="9" height="12" viewBox="0 0 9 12"><path d="M4.5 0C2 0 0 2 0 4.5 0 8 4.5 12 4.5 12S9 8 9 4.5C9 2 7 0 4.5 0Z" fill="#555"/><circle cx="4.5" cy="4.5" r="1.6" fill="#fff"/></svg>Los Angeles, California</span><b>$455,000</b></div>
    </article>
    <article class="listing">
      <div class="listing-photo p5" role="img" aria-label="Country home under a bright blue sky"><span class="listing-tag">NEW LISTING</span></div>
      <div class="listing-body">Four bedrooms, open kitchen and a wide deck facing the water, set on a quiet wooded lot.</div>
      <div class="listing-foot"><span><svg width="9" height="12" viewBox="0 0 9 12"><path d="M4.5 0C2 0 0 2 0 4.5 0 8 4.5 12 4.5 12S9 8 9 4.5C9 2 7 0 4.5 0Z" fill="#555"/><circle cx="4.5" cy="4.5" r="1.6" fill="#fff"/></svg>Los Angeles, California</span><b>$540,000</b></div>
    </article>
    <article class="listing">
      <div class="listing-photo p6" role="img" aria-label="Stone and brick manor with tall gables"><span class="listing-tag">NEW LISTING</span></div>
      <div class="listing-body">Four bedrooms, open kitchen and a wide deck facing the water, set on a quiet wooded lot.</div>
      <div class="listing-foot"><span><svg width="9" height="12" viewBox="0 0 9 12"><path d="M4.5 0C2 0 0 2 0 4.5 0 8 4.5 12 4.5 12S9 8 9 4.5C9 2 7 0 4.5 0Z" fill="#555"/><circle cx="4.5" cy="4.5" r="1.6" fill="#fff"/></svg>Los Angeles, California</span><b>$690,000</b></div>
    </article>
  </div>
</section>

<section class="news">
  <div class="news-head">
    <h2>LATEST NEWS</h2>
    <div class="news-arrows">
      <svg width="8" height="10" viewBox="0 0 8 10"><path d="M6 1 2 5l4 4" fill="none" stroke="#333" stroke-width="2"/></svg>
      <svg width="8" height="10" viewBox="0 0 8 10"><path d="M2 1l4 4-4 4" fill="none" stroke="#333" stroke-width="2"/></svg>
    </div>
  </div>
  <div class="news-list">
    <article class="news-item">
      <div class="news-photo n1" role="img" aria-label="Family home with front lawn in spring"></div>
      <div>
        <h3>Nulla at diam ornare, aliquam urna</h3>
        <div class="news-date">MAY 22, 2018</div>
        <p>Spring brings new homes to the market. Here is what buyers should know before touring lakeside properties this season.</p>
        <a class="news-more" href="#">Read More ›</a>
      </div>
    </article>
    <article class="news-item">
      <div class="news-photo n2" role="img" aria-label="Family outdoors in front of a new home"></div>
      <div>
        <h3>Nulla at diam ornare, aliquam urna</h3>
        <div class="news-date">MAY 22, 2018</div>
        <p>Spring brings new homes to the market. Here is what buyers should know before touring lakeside properties this season.</p>
        <a class="news-more" href="#">Read More ›</a>
      </div>
    </article>
  </div>
</section>

<footer class="site-footer">
  <div class="footer-brand">
    <span class="brand"><span class="brand-square"></span>HEARTHSIDE REALTY GROUP</span>
    <div class="social"><span></span><span></span><span></span><span></span></div>
  </div>
  <div class="footer-col contact">
    <h3>CONTACT US</h3>
    <ul>
      <li><svg width="9" height="12" viewBox="0 0 9 12"><path d="M4.5 0C2 0 0 2 0 4.5 0 8 4.5 12 4.5 12S9 8 9 4.5C9 2 7 0 4.5 0Z" fill="#ccc"/></svg><span>Hearthside Realty Group<br>218 Lakeview Drive, Suite 5, Harbor Springs</span></li>
      <li><svg width="11" height="11" viewBox="0 0 11 11"><path d="M2 0h2l1 3-1.5 1a7 7 0 0 0 3.5 3.5L8 6l3 1v2a2 2 0 0 1-2 2A9 9 0 0 1 0 2a2 2 0 0 1 2-2Z" fill="#ccc"/></svg><span>Phone: +1 (555) 014-2270</span></li>
      <li><svg width="12" height="9" viewBox="0 0 12 9"><rect width="12" height="9" fill="#ccc"/><path d="M0 0l6 5 6-5" fill="none" stroke="#121212" stroke-width="1.2"/></svg><span>hello@hearthside-realty.example</span></li>
    </ul>
  </div>
  <div class="footer-col signup">
    <h3>SIGN UP TO RECEIVE EMAIL</h3>
    <p>Get new listings and market updates sent straight to your inbox.</p>
    <div class="signup-input">Email address</div>
    <a class="signup-btn" href="#">SUBSCRIBE</a>
  </div>
  <div class="footer-col quick">
    <h3>QUICK LINKS</h3>
    <ul>
      <li>Home</li>
      <li>MyQV Info</li>
      <li>About My QV Home</li>
      <li>Download</li>
      <li>Contact Us</li>
    </ul>
  </div>
</footer>
<div class="copyright">Copyright © Hearthside Realty Group 2018. All rights reserved.</div>

</body>
</html>
```